Mirvane Trinkets
Lucinda Harrow Designs
Mirvane Trinkets -
Creative Brief
Simple
Lucinda Harrow
Jewelry Designer
2719 Quillfern Ln Dallas TX 75294
lucinda@mirvane-example.com
www.mirvane-example.com
Please do a few designs!
Maybe just the logo?

```html
<!DOCTYPE html>
<html lang="en">
<head>
<meta charset="utf-8">
<title>Mirvane Trinkets – Business Card</title>
<link rel="stylesheet" href="https://fonts.googleapis.com/css2?family=Open+Sans:wght@400;600;700&display=swap">
<style>
  :root {
    --backdrop: #ecebe8;
    --card-white: #ffffff;
    --teal-light: #1fe0d6;
    --teal-mid: #10aaa5;
    --teal-dark: #08807d;
    --silver: #c9cccd;
    --ink-teal: #15807e;
    --text-light: #ffffff;
  }
  html, body {
    margin: 0;
    padding: 0;
    width: 1200px;
    height: 935px;
    overflow: hidden;
    background: var(--backdrop);
    font-family: "Open Sans", Arial, sans-serif;
  }
  .business-card {
    position: absolute;
    left: 100px;
    top: 182px;
    width: 1000px;
    height: 571px;
    border-radius: 44px;
    overflow: hidden;
    background: var(--card-white);
    box-shadow: 0 6px 18px rgba(0,0,0,0.18);
  }
  .card-shapes {
    position: absolute;
    inset: 0;
    width: 100%;
    height: 100%;
  }
  .brand-lockup {
    position: absolute;
    left: 60px;
    top: 200px;
    width: 340px;
    display: flex;
    flex-direction: column;
    align-items: center;
    gap: 22px;
  }
  .brand-dot {
    width: 70px;
    height: 70px;
    border-radius: 50%;
    background: var(--silver);
  }
  .brand-name {
    margin: 0;
    font-size: 40px;
    font-weight: 400;
    color: var(--ink-teal);
    letter-spacing: 1px;
  }
  .person {
    position: absolute;
    right: 44px;
    top: 38px;
    text-align: right;
    color: var(--text-light);
  }
  .person-name {
    margin: 0;
    font-size: 33px;
    font-weight: 700;
  }
  .person-title {
    margin: 4px 0 0;
    font-size: 25px;
    font-weight: 600;
  }
  .contact {
    position: absolute;
    right: 44px;
    bottom: 38px;
    margin: 0;
    text-align: right;
    color: var(--text-light);
    font-style: normal;
    font-size: 23px;
    font-weight: 600;
    line-height: 1.45;
  }
</style>
</head>
<body>
  <section class="business-card">
    <svg class="card-shapes" viewBox="0 0 1000 571" aria-hidden="true">
      <defs>
        <radialGradient id="tealGlow" cx="0.7" cy="0.45" r="0.55">
          <stop offset="0" stop-color="var(--teal-light)"/>
          <stop offset="0.55" stop-color="var(--teal-mid)"/>
          <stop offset="1" stop-color="var(--teal-dark)"/>
        </radialGradient>
        <linearGradient id="silverEdge" x1="0" y1="0" x2="1" y2="0">
          <stop offset="0" stop-color="#ffffff" stop-opacity="0"/>
          <stop offset="1" stop-color="var(--silver)"/>
        </linearGradient>
      </defs>
      <path class="silver-swoosh" d="M 380 0 C 500 60, 540 200, 482 330 S 412 520, 432 571 L 452 571 C 432 520, 450 420, 500 330 S 520 60, 400 0 Z" fill="url(#silverEdge)"/>
      <path class="teal-panel" d="M 400 0 C 520 60, 560 200, 500 330 S 432 520, 452 571 L 1000 571 L 1000 0 Z" fill="url(#tealGlow)"/>
    </svg>

    <div class="brand-lockup">
      <span class="brand-dot"></span>
      <p class="brand-name">Mirvane Trinkets</p>
    </div>

    <div class="person">
      <p class="person-name">Lucinda Harrow</p>
      <p class="person-title">Jewelry Designer</p>
    </div>

    <address class="contact">
      2719 Quillfern Ln Dallas TX 75294<br>
      Phone : 214-555-0187<br>
      Email : lucinda@mirvane-example.com<br>
      Web : www.mirvane-example.com
    </address>
  </section>
</body>
</html>
```